Velmora Group
Velmora Financial
Velmora Group -
Creative Brief
Pirot Brekon
Partner
318 Elmwick Lane London E9 4PQ United Kingdom
Pbrekon@quillmesh.net
Company No. 5281947
Please provide an alternative design with the name Velmora Group instead of Velmora Financial
Just the logo

```html
<!DOCTYPE html>
<html lang="en">
<head>
<meta charset="utf-8">
<title>Velmora Group – Stationery Set</title>
<link href="https://fonts.googleapis.com/css2?family=Cinzel:wght@600&family=Cormorant+SC:wght@500;600&display=swap" rel="stylesheet">
<style>
  :root {
    --canvas: #ffffff;
    --frame: #e3e3e3;
    --paper: #ffffff;
    --paper-edge: #d9d9d9;
    --shadow: rgba(0, 0, 0, 0.22);
    --navy: #1f2a44;
    --blue: #3a78d0;
    --ink: #3a3a3a;
    --ghost: #eceef2;
    --flap-line: #b5b5b5;
  }
  * { box-sizing: border-box; margin: 0; padding: 0; }
  html, body { width: 1200px; height: 681px; overflow: hidden; background: var(--canvas); }
  .stage { position: relative; width: 1200px; height: 681px; background: var(--canvas); }
  .stage-frame {
    position: absolute; left: 12px; top: 12px; right: 12px; bottom: 12px;
    border: 1px solid var(--frame);
  }
  .sheet {
    position: absolute;
    background: var(--paper);
    border: 1px solid var(--paper-edge);
    box-shadow: 3px 4px 7px var(--shadow);
    overflow: hidden;
  }
  .brand {
    position: absolute; z-index: 1;
    display: flex; align-items: center; gap: 6px;
    font-family: "Cinzel", serif; font-weight: 600;
    color: var(--navy); letter-spacing: 0.04em; white-space: nowrap; line-height: 1;
  }
  .brand-mark { background: var(--blue); flex: none; }
  .address {
    position: absolute; z-index: 1;
    font-family: "Cormorant SC", serif; font-weight: 500;
    color: var(--ink); line-height: 1.3; white-space: nowrap;
  }
  .ghost-name {
    position: absolute; z-index: 0;
    font-family: "Cinzel", serif; font-weight: 600;
    color: var(--ghost); white-space: nowrap; line-height: 1;
  }

  /* Envelope front */
  .envelope-front { left: 53px; top: 106px; width: 355px; height: 199px; }
  .envelope-front .brand { left: 14px; top: 48px; font-size: 16px; }
  .envelope-front .brand-mark { width: 11px; height: 11px; }
  .envelope-front .address { left: 14px; top: 70px; font-size: 8px; }

  /* Envelope back */
  .envelope-back { left: 53px; top: 336px; width: 355px; height: 192px; }
  .envelope-back .flap { position: absolute; left: 0; top: 0; width: 355px; height: 56px; }
  .envelope-back .brand { left: 50%; top: 72px; transform: translateX(-50%); font-size: 14px; }
  .envelope-back .brand-mark { width: 10px; height: 10px; }

  /* Letterhead */
  .letterhead { left: 600px; top: 48px; width: 324px; height: 571px; }
  .letterhead .brand { left: 24px; top: 52px; font-size: 16px; }
  .letterhead .brand-mark { width: 11px; height: 11px; }
  .letterhead .address { left: 24px; top: 76px; font-size: 8px; }
  .letterhead .ghost-name { right: 14px; bottom: 26px; font-size: 46px; }

  /* Business cards */
  .card-front { left: 970px; top: 178px; width: 168px; height: 93px; }
  .card-front .brand { left: 80px; top: 14px; font-size: 7px; gap: 3px; }
  .card-front .brand-mark { width: 5px; height: 5px; }
  .card-front .person {
    position: absolute; z-index: 1; left: 80px; top: 28px;
    font-family: "Cormorant SC", serif; color: var(--navy); line-height: 1.15;
  }
  .card-front .person-name { font-size: 6px; font-weight: 600; }
  .card-front .person-role { font-size: 5px; font-weight: 500; }
  .card-front .address { left: 80px; top: 48px; font-size: 4px; }
  .card-front .ghost-name { left: 140px; top: 58px; font-size: 30px; }

  .card-back { left: 970px; top: 288px; width: 168px; height: 110px; }
  .card-back .brand { left: 50%; top: 50px; transform: translateX(-50%); font-size: 11px; gap: 4px; }
  .card-back .brand-mark { width: 8px; height: 8px; }
</style>
</head>
<body>
<main class="stage">
  <div class="stage-frame"></div>

  <section class="sheet envelope-front" aria-label="Envelope front">
    <div class="brand"><span class="brand-mark"></span>Velmora Group</div>
    <p class="address">318 Elmwick Lane<br>London E9 4PQ United Kingdom</p>
  </section>

  <section class="sheet envelope-back" aria-label="Envelope back">
    <svg class="flap" viewBox="0 0 355 56" aria-hidden="true">
      <path d="M0 4 Q14 4 26 38 Q30 48 44 48 L311 48 Q325 48 329 38 Q341 4 355 4" fill="none" stroke="var(--flap-line)" stroke-width="1"/>
    </svg>
    <div class="brand"><span class="brand-mark"></span>Velmora Group</div>
  </section>

  <section class="sheet letterhead" aria-label="Letterhead">
    <div class="brand"><span class="brand-mark"></span>Velmora Group</div>
    <p class="address">318 Elmwick Lane<br>London E9 4PQ United Kingdom<br>Telephone: +44(0)20 7946 0381</p>
    <div class="ghost-name" aria-hidden="true">Velmora</div>
  </section>

  <section class="sheet card-front" aria-label="Business card front">
    <div class="brand"><span class="brand-mark"></span>Velmora Group</div>
    <div class="person">
      <p class="person-name">Pirot Brekon</p>
      <p class="person-role">Partner</p>
    </div>
    <p class="address">318 Elmwick Lane<br>London E9 4PQ<br>Mobile: 07700 900461<br>Pbrekon@quillmesh.net<br>Company No. 5281947</p>
    <div class="ghost-name" aria-hidden="true">V</div>
  </section>

  <section class="sheet card-back" aria-label="Business card back">
    <div class="brand"><span class="brand-mark"></span>Velmora Group</div>
  </section>
</main>
</body>
</html>
```